Help me make landing pages for my web application that are mobile friendly

I need to make 2 mobile friendly landing pages for an application. The 2 pages will be related. First I need a home page and then I need a working page. I do not want to change the color scheme or logos. Just layout and design.

```html
<!DOCTYPE html>
<html lang="en">
<head>
<meta charset="UTF-8">
<title>ShiftCover – Opening Information</title>
<link rel="stylesheet" href="https://fonts.googleapis.com/css2?family=Figtree:wght@600;700&family=Poppins:wght@400;500;600&display=swap">
<style>
  :root {
    --page-bg: #ffffff;
    --brand: #5b3f93;
    --brand-soft: #6a4fa3;
    --panel: #171717;
    --panel-raised: #2b2b2b;
    --field: #252525;
    --field-raised: #3a3a3a;
    --chip: #1c1c1c;
    --text: #ffffff;
    --text-muted: #c9c9c9;
    --track: #3a3a3a;
  }
  * { box-sizing: border-box; margin: 0; padding: 0; }
  html, body { width: 778px; height: 1200px; overflow: hidden; background: var(--page-bg); }
  body { position: relative; font-family: "Poppins", sans-serif; color: var(--text); }

  .screen {
    position: absolute; left: 172px; top: 180px; width: 422px; height: 892px;
    border-radius: 42px; overflow: hidden; background: var(--brand);
  }
  .header { position: absolute; inset: 0 0 auto 0; height: 160px; background: linear-gradient(160deg, var(--brand) 0%, var(--brand-soft) 100%); }

  .status-bar { position: absolute; left: 38px; right: 38px; top: 20px; height: 18px; display: flex; align-items: center; justify-content: space-between; }
  .status-time { font-family: "Figtree", sans-serif; font-weight: 700; font-size: 14px; }
  .status-icons { display: flex; gap: 10px; align-items: center; }

  .brand-name { position: absolute; left: 104px; top: 62px; font-family: "Figtree", sans-serif; font-weight: 600; font-size: 32px; letter-spacing: -0.3px; }
  .header-actions { position: absolute; right: 38px; top: 70px; display: flex; gap: 6px; }
  .icon-button { width: 31px; height: 31px; border-radius: 7px; background: var(--chip); display: flex; align-items: center; justify-content: center; }

  .content { position: absolute; left: 0; right: 0; top: 140px; bottom: 0; background: var(--panel); border-radius: 46px 46px 0 0; }
  .section-title { position: absolute; font-family: "Figtree", sans-serif; font-weight: 700; font-size: 20px; }
  .field-label { position: absolute; font-family: "Figtree", sans-serif; font-weight: 700; font-size: 13px; }
  .field { position: absolute; height: 40px; border-radius: 8px; background: var(--field); font-size: 11px; color: var(--text-muted); padding: 12px 0 0 25px; }
  .field-wide { width: 351px; }
  .field-half { width: 170px; }
  .field-tall { height: 95px; }

  .scrollbar { position: absolute; left: 404px; top: 225px; width: 3px; height: 535px; background: var(--track); border-radius: 2px; }
  .scrollbar-thumb { position: absolute; left: 0; top: 0; width: 3px; height: 125px; background: var(--brand-soft); border-radius: 2px; }

  .comments { position: absolute; left: 0; right: 0; top: 582px; bottom: 0; background: var(--panel-raised); border-radius: 46px 46px 0 0; }
  .comment-input { position: absolute; left: 35px; top: 58px; width: 299px; height: 95px; border-radius: 8px; background: var(--field-raised); font-size: 11px; color: var(--text-muted); padding: 16px 0 0 25px; }
  .action-button { position: absolute; left: 343px; width: 43px; height: 42px; border-radius: 9px; background: var(--brand); display: flex; align-items: center; justify-content: center; }

  .tab-bar { position: absolute; left: 15px; top: 815px; width: 393px; height: 68px; border-radius: 34px; background: var(--brand); display: flex; justify-content: space-around; align-items: center; padding: 0 14px; }
  .tab { display: flex; flex-direction: column; align-items: center; gap: 3px; font-family: "Figtree", sans-serif; font-weight: 700; font-size: 12px; width: 70px; }
  .scrollbar-sub { position: absolute; left: 404px; top: 0; }
</style>
</head>
<body>
  <main class="screen">
    <header class="header">
      <div class="status-bar">
        <span class="status-time">10:56</span>
        <span class="status-icons">
          <svg width="14" height="12" viewBox="0 0 14 12" fill="#fff"><rect x="0" y="8" width="2" height="4"/><rect x="4" y="5" width="2" height="7"/><rect x="8" y="2" width="2" height="10" opacity=".5"/><rect x="12" y="0" width="2" height="12" opacity=".5"/></svg>
          <svg width="17" height="12" viewBox="0 0 17 12" fill="none" stroke="#fff" stroke-width="1.8" stroke-linecap="round"><path d="M1 4a11 11 0 0 1 15 0"/><path d="M3.5 7a7 7 0 0 1 10 0"/><circle cx="8.5" cy="10.5" r="1" fill="#fff" stroke="none"/></svg>
          <svg width="22" height="11" viewBox="0 0 22 11"><rect x="0.5" y="0.5" width="19" height="10" rx="2" fill="none" stroke="#fff"/><rect x="2" y="2" width="16" height="7" rx="1" fill="#fff"/><rect x="20" y="3.5" width="1.5" height="4" fill="#fff"/></svg>
        </span>
      </div>
      <div class="brand-name">ShiftCover</div>
      <div class="header-actions">
        <span class="icon-button"><svg width="13" height="13" viewBox="0 0 13 13" fill="#fff"><circle cx="6.5" cy="3.5" r="3"/><path d="M1 13a5.5 5 0 0 1 11 0z"/></svg></span>
        <span class="icon-button"><svg width="15" height="12" viewBox="0 0 15 12" stroke="#fff" stroke-width="1.4" stroke-linecap="round"><path d="M4 1h10M1 6h13M7 11h7"/></svg></span>
      </div>
    </header>

    <section class="content">
      <h1 class="section-title" style="left:34px;top:36px">Opening Information</h1>

      <span class="field-label" style="left:55px;top:81px">Summary</span>
      <span class="field-label" style="left:235px;top:81px">Location</span>
      <div class="field field-half" style="left:35px;top:106px">Testing-test</div>
      <div class="field field-half" style="left:216px;top:106px">Cedar Grove Elementary</div>

      <span class="field-label" style="left:55px;top:155px">Type</span>
      <span class="field-label" style="left:235px;top:155px">Regular Staff</span>
      <div class="field field-half" style="left:35px;top:180px">Vacancy</div>
      <div class="field field-half" style="left:216px;top:180px">Maya Ortiz</div>

      <span class="field-label" style="left:55px;top:229px">Assignment Category</span>
      <span class="field-label" style="left:235px;top:229px">Department</span>
      <div class="field field-half" style="left:35px;top:254px">Teacher</div>
      <div class="field field-half" style="left:216px;top:254px"></div>

      <span class="field-label" style="left:55px;top:304px">Description</span>
      <div class="field field-wide field-tall" style="left:35px;top:329px;padding-top:17px">Teacher</div>

      <section class="comments">
        <h2 class="section-title" style="left:34px;top:26px">Comments</h2>
        <div class="comment-input">Write a comment or uploaded file...</div>
        <span class="action-button" style="top:60px">
          <svg width="19" height="17" viewBox="0 0 19 17" fill="#fff"><path d="M18 1 1 7.5l6 2.5 1 6 3-4.5 4 2.5z"/><path d="M7 10 18 1" stroke="#5b3f93" stroke-width="1.3"/></svg>
        </span>
        <span class="action-button" style="top:111px">
          <svg width="14" height="18" viewBox="0 0 14 18"><rect x="0" y="0" width="14" height="18" rx="2.5" fill="#fff"/><path d="M7 12V5M4.3 7.5 7 4.8l2.7 2.7M4 14h6" stroke="#5b3f93" stroke-width="1.6" fill="none" stroke-linecap="round"/></svg>
        </span>
        <h2 class="section-title" style="left:34px;top:165px">Additional Details</h2>
        <div class="field field-wide" style="left:35px;top:197px">Parking Spot</div>
      </section>

      <div class="scrollbar"><div class="scrollbar-thumb"></div></div>
    </section>

    <nav class="tab-bar">
      <span class="tab"><svg width="20" height="20" viewBox="0 0 20 20"><circle cx="10" cy="10" r="10" fill="#fff"/><path d="M5.5 10 10 5.8l4.5 4.2v4.5h-3v-3h-3v3h-3z" fill="#5b3f93"/></svg>Home</span>
      <span class="tab"><svg width="20" height="20" viewBox="0 0 20 20"><circle cx="10" cy="10" r="10" fill="#fff"/><circle cx="10" cy="7.5" r="3" fill="#5b3f93"/><path d="M4.5 16a5.5 4.5 0 0 1 11 0z" fill="#5b3f93"/></svg>Profile</span>
      <span class="tab"><svg width="24" height="20" viewBox="0 0 24 20"><path d="M4 11a8 8 0 0 1 16 0" stroke="#fff" stroke-width="2" fill="none"/><rect x="2" y="10" width="4" height="6" rx="1.5" fill="#fff"/><rect x="18" y="10" width="4" height="6" rx="1.5" fill="#fff"/><ellipse cx="12" cy="11" rx="6" ry="5" fill="#fff"/><circle cx="9.5" cy="11" r="1" fill="#5b3f93"/><circle cx="12" cy="11" r="1" fill="#5b3f93"/><circle cx="14.5" cy="11" r="1" fill="#5b3f93"/></svg>Support</span>
      <span class="tab"><svg width="20" height="20" viewBox="0 0 20 20" fill="none" stroke="#fff" stroke-width="2" stroke-linecap="round"><path d="M3.5 6A8 8 0 1 1 2 10"/><path d="M3 2v4h4"/><path d="M10 6v4.5l3 2"/></svg>History</span>
      <span class="tab"><svg width="20" height="20" viewBox="0 0 20 20" fill="#fff"><rect x="1" y="1" width="8" height="8" rx="2"/><rect x="11" y="1" width="8" height="8" rx="2"/><rect x="1" y="11" width="8" height="8" rx="2"/><rect x="11.5" y="11.5" width="7" height="7" rx="1" transform="rotate(45 15 15)"/></svg>More</span>
    </nav>
  </main>
</body>
</html>
```